Energy trading company (Voltrisa) needs a business card

We need a business card for a company based in Central America. Our main purpose is trading energy . We already have the logo but we need some good creativity to design a high impact business card. Colors blue, orange, green can be used or we would like to see good combinatios with our logo

Target Market(s)

Energy

Industry/Entity Type

Power Generation

Contact Information for Business Card

Logo , headquarters , name, background

Font styles to use
Serif
Sans Serif

Colors

Designer to choose colors to be used in the design.

Requirements
Must have
• it must have a fresh and clean view
Nice to have
• good backgrounds that combine with the logo
Should not have
• too much words

```html
<!DOCTYPE html>
<html lang="en">
<head>
<meta charset="utf-8">
<title>Voltrisa business card</title>
<link href="https://fonts.googleapis.com/css2?family=Roboto:wght@400;500&family=Saira+Semi+Condensed:wght@600&display=swap" rel="stylesheet">
<style>
  :root {
    --stage: #bcbcbc;
    --card: #f4f4f3;
    --orange: #e07f1c;
    --ink: #2e2e2e;
    --blue: #0c5590;
    --green: #3e9a35;
  }
  * { margin: 0; padding: 0; box-sizing: border-box; }
  html, body { width: 1200px; height: 576px; overflow: hidden; }
  body {
    background: var(--stage);
    font-family: "Roboto", Arial, sans-serif;
    color: var(--ink);
    position: relative;
  }
  .card {
    position: absolute;
    top: 140px;
    width: 484px;
    height: 292px;
    background: var(--card);
    border-radius: 10px;
    overflow: hidden;
  }
  .card--front { left: 82px; }
  .card--back { left: 602px; }

  .brand-mark {
    position: absolute;
    width: 70px; height: 70px;
    border-radius: 50%;
    background: var(--orange);
  }
  .brand-name {
    position: absolute;
    font-family: "Roboto", Arial, sans-serif;
    font-weight: 500;
    color: var(--orange);
    letter-spacing: 1px;
    line-height: 1;
    white-space: nowrap;
  }

  .card--front .brand-mark { left: 207px; top: 60px; }
  .card--front .brand-name { left: 0; width: 100%; text-align: center; top: 160px; font-size: 48px; }

  .front-url {
    position: absolute;
    left: 0; width: 100%;
    top: 255px;
    text-align: center;
    font-size: 13px;
  }
  .front-url::before, .front-url::after {
    content: "";
    display: inline-block;
    width: 32px; height: 2px;
    background: var(--orange);
    vertical-align: middle;
    margin: 0 28px;
  }
  .color-band {
    position: absolute;
    left: 0; bottom: 0;
    width: 100%; height: 13px;
    display: flex;
  }
  .color-band span { flex: 1; }
  .color-band .band-blue { background: var(--blue); }
  .color-band .band-green { background: var(--green); }

  .holder-name {
    position: absolute;
    left: 31px; top: 44px;
    font-family: "Saira Semi Condensed", Arial, sans-serif;
    font-weight: 600;
    font-size: 20px;
    color: var(--orange);
  }
  .holder-role {
    position: absolute;
    left: 31px; top: 70px;
    font-size: 13px;
  }
  .card--back .brand-mark { left: 340px; top: 28px; width: 58px; height: 58px; }
  .card--back .brand-name { right: 28px; top: 115px; font-size: 37px; }

  .contact-list {
    position: absolute;
    left: 31px; top: 188px;
    list-style: none;
    font-size: 13px;
  }
  .contact-list li {
    display: flex;
    align-items: center;
    height: 18.5px;
  }
  .contact-list svg { width: 11px; height: 11px; margin: 0 14px 0 1px; fill: var(--orange); }
  .address {
    position: absolute;
    left: 31px; top: 249px;
    font-size: 13px;
  }
</style>
</head>
<body>
  <section class="card card--front">
    <div class="brand-mark"></div>
    <div class="brand-name">VOLTRISA</div>
    <div class="front-url">www.voltrisa.com</div>
    <div class="color-band"><span class="band-blue"></span><span class="band-green"></span></div>
  </section>

  <section class="card card--back">
    <div class="holder-name">Mara Ellison Vance</div>
    <div class="holder-role">Managing Director</div>
    <div class="brand-mark"></div>
    <div class="brand-name">VOLTRISA</div>
    <ul class="contact-list">
      <li>
        <svg viewBox="0 0 12 12" aria-hidden="true"><path d="M1 3.5C1 2 3 1.2 6 1.2S11 2 11 3.5L9 4.3 8.2 3H3.8L3 4.3ZM2.5 5.5h7L10.5 11h-9Z"/><circle cx="6" cy="7.8" r="1.4" fill="#f4f4f3"/></svg>
        <span>555-014-2290</span>
      </li>
      <li>
        <svg viewBox="0 0 12 12" aria-hidden="true"><path d="M0.5 2.5h11v7h-11Z"/><path d="M0.8 2.8L6 6.8 11.2 2.8" fill="none" stroke="#f4f4f3" stroke-width="1"/></svg>
        <span>mara@voltrisa.com</span>
      </li>
      <li>
        <svg viewBox="0 0 12 12" aria-hidden="true"><circle cx="6" cy="6" r="5.3"/><path d="M0.7 6h10.6M6 0.7v10.6M2 3.3h8M2 8.7h8" stroke="#f4f4f3" stroke-width="0.7" fill="none"/><ellipse cx="6" cy="6" rx="2.4" ry="5.3" fill="none" stroke="#f4f4f3" stroke-width="0.7"/></svg>
        <span>www.voltrisa.com</span>
      </li>
    </ul>
    <div class="address">418 Meridian Ave., Harbor City, Lakeview, US 204718</div>
  </section>
</body>
</html>
```